Mezzanine Floor Manufacturer looking for a new business card design

We manufacture mezzanine floors and are providers of racking systems. We provide a range of items/services - simple rack repairs , full warehouse fit outs , manufacturer and install mezzanine floors , partitioning and large turnkey projects. Recently had a new website - www.corrowden-racking.co.uk and would like our business cards updating aswell . Our current card is single sided in the old logo colours (pdf attached) and needs updating.

Target Market(s)

We deal with large projects/ multi national companies and also smaller projects and companies throughout the UK ranging from a single warehouse to a large multi site company.

Industry/Entity Type

Business

Contact Information for Business Card

Will have job title,tel no's, email ,website address etc like example pdf

Requirements
Must have
• Hi - needs to use the colours of the logo & new website. Card needs to be professional

```html
<!DOCTYPE html>
<html lang="en">
<head>
<meta charset="utf-8">
<title>Corrowden Business Card</title>
<link rel="stylesheet" href="https://fonts.googleapis.com/css2?family=Roboto+Condensed:wght@400;700&family=Exo+2:wght@400&display=swap">
<style>
  :root{
    --bg:#9a9a9a;
    --card-white:#f7f7f5;
    --card-black:#141414;
    --red:#d3272d;
    --ink:#1c1c1c;
    --grey:#3a3a3a;
    --faint:#202020;
  }
  *{margin:0;padding:0;box-sizing:border-box}
  html,body{width:1200px;height:800px;overflow:hidden}
  body{background:var(--bg);position:relative;font-family:"Roboto Condensed",sans-serif}
  .card{position:absolute;top:245px;width:540px;height:310px;box-shadow:0 6px 18px rgba(0,0,0,.25);overflow:hidden}
  .card--front{left:40px;background:var(--card-white)}
  .card--back{left:620px;background:var(--card-black)}

  .brand{position:absolute;display:flex;align-items:center;gap:10px}
  .brand__dot{width:22px;height:22px;border-radius:50%;background:var(--red)}
  .brand__name{font-family:"Roboto Condensed",sans-serif;font-weight:700;color:var(--red);letter-spacing:1px}
  .card--front .brand{left:30px;top:34px}
  .card--front .brand__name{font-size:30px}

  .person{position:absolute;right:30px;top:28px;text-align:right}
  .person__name{font-weight:700;font-size:30px;color:var(--ink);letter-spacing:-.3px;line-height:1}
  .person__role{font-size:15px;color:var(--grey);margin-top:2px}
  .rule{position:absolute;left:240px;right:30px;top:88px;height:2px;background:var(--red)}

  .services{position:absolute;right:30px;top:100px;list-style:none;text-transform:uppercase;font-size:15px;color:var(--ink);line-height:19px}
  .services li::before{content:"";display:inline-block;width:5px;height:5px;border-radius:50%;background:var(--red);margin-right:7px;vertical-align:middle}

  .contact{position:absolute;left:30px;bottom:24px;list-style:none;font-family:"Exo 2",sans-serif;font-size:15px;color:var(--ink);line-height:24px}
  .contact li{display:flex;align-items:center;gap:12px}
  .contact svg{width:15px;height:15px;fill:none;stroke:var(--red);stroke-width:2;stroke-linecap:round;stroke-linejoin:round}

  .watermark{position:absolute;left:24px;top:34px;font-weight:700;font-size:68px;line-height:1;color:var(--faint);letter-spacing:2px}
  .card--back .brand{right:36px;top:128px}
  .card--back .brand__name{font-size:34px}
  .card--back .brand__dot{width:26px;height:26px}
  .address{position:absolute;left:30px;bottom:28px;color:var(--red);font-size:15px;line-height:20px;font-family:"Exo 2",sans-serif}
</style>
</head>
<body>
  <section class="card card--front">
    <div class="brand"><span class="brand__dot"></span><span class="brand__name">CORROWDEN</span></div>
    <div class="person">
      <div class="person__name">DANIEL HARTLEY</div>
      <div class="person__role">technical sales</div>
    </div>
    <div class="rule"></div>
    <ul class="services">
      <li>Mezzanine Floors</li>
      <li>Cantilever Racking</li>
      <li>Pallet Racking</li>
      <li>Safety Barriers</li>
      <li>Longspan Shelving</li>
      <li>Steel Shelving</li>
      <li>Partitioning</li>
      <li>Turnkey Projects</li>
    </ul>
    <ul class="contact">
      <li><svg viewBox="0 0 16 16"><path d="M3 2h3l1 3-2 1.5a8 8 0 0 0 4.5 4.5L11 9l3 1v3a1 1 0 0 1-1 1A12 12 0 0 1 2 3a1 1 0 0 1 1-1z"/></svg>01632 960481</li>
      <li><svg viewBox="0 0 16 16"><rect x="4" y="1.5" width="8" height="13" rx="1.5"/><path d="M7 12h2"/></svg>07700 900317</li>
      <li><svg viewBox="0 0 16 16"><rect x="2" y="6" width="12" height="6" rx="1"/><path d="M4.5 6V2h7v4M4.5 10h7v4h-7z"/></svg>01632 960599</li>
      <li><svg viewBox="0 0 16 16"><rect x="1.5" y="3.5" width="13" height="9" rx="1"/><path d="M1.5 4l6.5 5 6.5-5"/></svg>daniel@corrowden-racking.co.uk</li>
      <li><svg viewBox="0 0 16 16"><circle cx="8" cy="8" r="6.5"/><path d="M1.5 8h13M8 1.5c2.5 2.5 2.5 10.5 0 13M8 1.5c-2.5 2.5-2.5 10.5 0 13"/></svg>www.corrowden-racking.co.uk</li>
    </ul>
  </section>

  <section class="card card--back">
    <div class="watermark" aria-hidden="true">CORROWDEN</div>
    <div class="brand"><span class="brand__dot"></span><span class="brand__name">CORROWDEN</span></div>
    <p class="address">Mill Brook Close Ashfield Gate Business<br>Park Holmby, Derbyshire DE9 4QT</p>
  </section>
</body>
</html>
```